■サイトマップ
★:Gナビに掲載希望

TOP ★
写真館のこと ★
料金一覧 ★
店舗情報 ★
スタッフ紹介
ギャラリー ★
お子さまの成長の記念に(七五三)
思い出やこだわりにあわせた屋外撮影(ロケーション・出張撮影)
季節限定!キャンペーンフォト
キッズ・ベビー・お宮参りの撮影もおまかせください
成人の節目に晴れ姿を撮影
入園・入学・卒業
そのほかの撮影
よくある質問 ★
お問い合わせ(追従ボタン)
ブログ
ニュース

※お子さまの記念~そのほかの撮影のページ
「撮影のこだわり」という文言をGナビに配置して
プルダウンで表示させたいです。

■ターゲット
30~40代 主婦層にあわせて作る
店舗へ電話をかけてくるのはお母さんのため。

■TOPで目立たせたいコンテンツ
・季節限定!キャンペーンフォト
・思い出やこだわりにあわせた屋外撮影(ロケーション・出張撮影)

■上記以外でTOPに掲載したいコンテンツ
・ギャラリー
・写真館のこと
・七五三
・ブログ(更新頻度は低め)
・ニュース(更新頻度は低め)
・元気いっぱいなお子さまの撮影はお任せください!(リンクなし)
・スタッフ紹介

■デザインについて
・英語表記をする際は日本語表記もそえてください。
・Gナビを英語表記にする際は、オンカーソルで日本語表記が出るようにしてほしいです。
・子供の写真は幼稚園~小学校くらいの年齢をメインにしてください。
・キャンペーンページへの追従ボタンを配置。
・メインスライドは大きく、写真がよく見えるように。
・画像を大きめに載せたいです。

■デザイン参考サイト
http://tidewell-nara.jp/
業種やことなりますが、Gナビがおしゃれです。

https://www.lumiane-atelier.com/
シンプルで遊び心が感じられます。
手書き風のイラストがかわいいです。

https://www.oxbel-net.com/kids/
撮影メニュー・催事の項目で取り扱いプランの一覧がわかっていいです。

■フォントについて
WEB上で使用可能な無料のフォントで作成お願い致します。
OSに紐づくフォントの使用は控えていただければと思います。
(ヒラギノなど)

===============================
●ロゴ
https://filevaultro.jp/download/8b1e27d3a06f4c95e2d7b18a3f60c4e7d9a2b5f1
ダウンロードパスワード 7rmx3pzt

●素材
https://filevaultro.jp/download/9c7d31e4b25a8f06d1e3c7b49a2f5e8d0b6c3a72
ダウンロードパスワード 7rmx3pzt
http://www.kt-hanamura.com/
茶系、緑系、グレー系
◆文言について
現行サイトの文章を使用してOKです。

◆素材について
素材として必要なものがある場合には、Velmora Stock画像をご使用ください。
その際、通常アセットでダウンロード出来る画像のみを使用してください。
Velmora Stock以外の素材を使用する際には、
必ず無料で提供いただける物のみご使用ください。

◆注意
店舗へ直接の問い合わせはおやめください。
すでに案をご提出くださった方々、ご応募いただきありがとうございます。
せっかくですので開催期間を延長したいと思います。
何卒よろしくお願いいたします。

雰囲気がにぎやかすぎず渋すぎず、ちょうどよかったため。

この度は選定について大変お待たせいたしました。
また機会がありましたら何卒よろしくお願いいたします。

```html
<!DOCTYPE html>
<html lang="ja">
<head>
<meta charset="utf-8">
<title>写真館 トップページ デザイン案</title>
<link rel="stylesheet" href="https://fonts.googleapis.com/css2?family=Noto+Serif+JP:wght@400;600&family=Zen+Maru+Gothic:wght@400;700&display=swap">
<style>
:root{
  --board:#ffffff;
  --cream:#f6f4ef;
  --paper:#fbfaf7;
  --tan:#d9cbb8;
  --tan-deep:#c9b79e;
  --brown:#8a6a4c;
  --brown-dark:#5a4432;
  --ink:#4a3d33;
  --muted:#8d8278;
  --green:#b9cf7c;
  --green-deep:#7e9a3f;
  --line:#e2dbd1;
}
*{box-sizing:border-box;margin:0;padding:0}
html,body{width:848px;height:1200px;overflow:hidden;background:var(--board)}
body{position:relative;font-family:"Zen Maru Gothic",sans-serif;color:var(--ink)}

.page{position:absolute;left:57px;top:23px;width:360px;height:1152px;background:var(--paper);box-shadow:0 0 0 1px var(--line);overflow:hidden}
.photo{border-radius:1px}
.btn{display:inline-block;background:var(--brown);color:#fff;font-size:5px;line-height:1;padding:3px 12px;letter-spacing:.1em}
.sec-title{font-family:"Noto Serif JP",serif;font-weight:600;font-size:8px;line-height:1.4;color:var(--brown-dark);letter-spacing:.08em}
.sec-title small{display:block;font-size:4.5px;font-weight:400;color:var(--muted);margin-top:1px}
.txt{font-size:4.5px;line-height:1.6;color:var(--muted)}

.hero{position:relative;height:141px;background:linear-gradient(160deg,#e7c3d6 0%,#d3a3c4 35%,#b488ad 60%,#8c9a5c 100%)}
.hero-photo{position:absolute;inset:0;background:radial-gradient(ellipse at 55% 55%,rgba(120,90,70,.35),transparent 30%)}
.site-bar{position:absolute;left:0;right:0;top:0;height:17px;background:rgba(255,255,255,.92);display:flex;align-items:center;padding:0 8px;gap:10px}
.logo{font-family:"Noto Serif JP",serif;font-size:7px;color:var(--brown-dark);display:flex;align-items:center;gap:3px}
.logo i{width:5px;height:5px;border-radius:50%;background:var(--brown)}
.gnav{display:flex;gap:8px;list-style:none;font-size:4.5px;color:var(--ink);letter-spacing:.06em}
.tel-mini{margin-left:auto;font-size:4.5px;background:var(--brown);color:#fff;padding:2px 5px}
.hero-copy{position:absolute;left:22px;top:62px;font-family:"Noto Serif JP",serif;color:#fff;font-size:10px;line-height:1.7;letter-spacing:.1em;text-shadow:0 0 4px rgba(80,40,60,.4)}

.intro{height:198px;background:var(--cream);padding:10px 12px;display:grid;grid-template-columns:90px 1fr 90px;grid-template-rows:66px 1fr;gap:8px}
.intro .center{text-align:center;padding-top:4px}
.intro .center .txt{margin:4px 0 5px}
.loc-text{grid-column:1/2;padding-top:14px}
.loc-text .txt{margin:4px 0 8px}
.loc-photo{grid-column:2/4}

.shichigosan{height:142px;background:var(--paper);padding:8px 12px;display:grid;grid-template-columns:1fr 1fr 120px;gap:6px}
.shichigosan .side{padding-top:34px;text-align:center}
.shichigosan .side .txt{margin:4px 0 8px}

.gallery{height:198px;background:var(--tan);padding:10px 20px 12px;display:flex;flex-direction:column;align-items:center;justify-content:space-between;text-align:center}
.gallery-row{display:grid;grid-template-columns:repeat(4,1fr);gap:5px;width:100%}
.gallery-row .photo{height:46px}

.kids{height:98px;background:var(--cream);padding:8px 12px;display:grid;grid-template-columns:60px 60px 1fr;gap:6px}
.kids .side{padding-top:22px;text-align:center}
.kids .side .txt{margin:3px 0 6px}

.staff{height:86px;background:var(--tan);padding:8px 40px;display:grid;grid-template-columns:120px 1fr;gap:12px;align-items:center}
.staff .txt{margin:3px 0 6px}

.info{height:98px;background:#fff;padding:10px 22px;display:grid;grid-template-columns:1fr 1fr;gap:18px}
.list{list-style:none;margin-top:5px}
.list li{font-size:4.5px;color:var(--muted);border-bottom:1px solid var(--line);padding:3px 0}
.thumbs{display:grid;grid-template-columns:repeat(3,1fr);gap:4px;margin-top:5px}
.thumbs .photo{height:26px}

.contact{height:100px;background:var(--green);display:flex;align-items:center;justify-content:center;gap:16px;color:var(--brown-dark)}
.contact .tel{font-family:"Noto Serif JP",serif;font-size:13px;letter-spacing:.06em;display:flex;align-items:center;gap:4px}
.contact .tel small{display:block;font-size:4.5px;font-family:"Zen Maru Gothic",sans-serif}
.contact .btn{background:var(--brown-dark);padding:5px 14px}

.footer{height:89px;background:#fff;padding:12px 18px;display:grid;grid-template-columns:130px 1fr;gap:12px}
.footer .name{font-family:"Noto Serif JP",serif;font-size:14px;color:var(--brown-dark);letter-spacing:.1em;display:flex;align-items:center;gap:5px}
.footer .name i{width:8px;height:8px;background:var(--brown)}
.footer .txt{margin-top:4px}
.map{background:linear-gradient(135deg,#e8e6e1,#d5d9cf)}

.fv-label{position:absolute;left:458px;top:22px;font-size:9px;color:var(--ink);letter-spacing:.05em}
.fv{position:absolute;left:453px;width:362px}
.fv-1{top:40px;height:135px;background:linear-gradient(120deg,#a9c27a 0%,#e9eedc 45%,#c8d9a3 100%)}
.fv-2{top:187px;height:141px;background:linear-gradient(110deg,#2d2a27 0%,#4a443c 35%,#d9cfc4 70%,#efe9e2 100%)}
.fv-2 .fv-copy{position:absolute;left:26px;top:58px;color:#fff;font-family:"Noto Serif JP",serif;font-size:8px;line-height:1.6;letter-spacing:.1em}
.fv-2 .fv-copy b{font-weight:600;font-size:10px}
</style>
</head>
<body>

<main class="page">
  <header class="hero">
    <div class="hero-photo photo" role="img" aria-label="コスモス畑の中で花を持つ子どもの写真"></div>
    <div class="site-bar">
      <div class="logo"><i></i>写真館</div>
      <ul class="gnav">
        <li>ABOUT</li><li>PRICE</li><li>SHOP</li><li>GALLERY</li><li>Q&amp;A</li>
      </ul>
      <span class="tel-mini">CAMPAIGN</span>
    </div>
    <p class="hero-copy">生まれてきてくれて<br>輝いた一瞬を<br>形に残そう</p>
  </header>

  <section class="intro">
    <div class="photo" role="img" aria-label="屋外で手をつなぐ家族の写真" style="background:linear-gradient(135deg,#b8c79a,#e2dccb)"></div>
    <div class="center">
      <h2 class="sec-title">写真館のこと<small>ABOUT</small></h2>
      <p class="txt">家族の大切な時間を<br>心をこめて撮影します</p>
      <span class="btn">MORE</span>
    </div>
    <div class="photo" role="img" aria-label="公園で遊ぶ子どもの写真" style="background:linear-gradient(135deg,#9fb57a,#d9d4c2)"></div>
    <div class="loc-text">
      <h2 class="sec-title">ロケーション<br>出張撮影<small>LOCATION</small></h2>
      <p class="txt">思い出の場所で<br>自然な笑顔を撮影</p>
      <span class="btn">MORE</span>
    </div>
    <div class="loc-photo photo" role="img" aria-label="木陰のベンチに座る家族の屋外写真" style="background:linear-gradient(120deg,#7f9a55,#c4cf9e 60%,#e6e0cc)"></div>
  </section>

  <section class="shichigosan">
    <div class="photo" role="img" aria-label="着物姿の母と子の写真" style="background:linear-gradient(160deg,#c9b6a6,#8c6f5c)"></div>
    <div class="photo" role="img" aria-label="晴れ着の子どもの写真" style="background:linear-gradient(160deg,#e5d3c6,#b98e84)"></div>
    <div class="side">
      <h2 class="sec-title">七五三<small>SHICHIGOSAN</small></h2>
      <p class="txt">お子さまの成長の<br>記念に残す一枚を</p>
      <span class="btn">MORE</span>
    </div>
  </section>

  <section class="gallery">
    <h2 class="sec-title">GALLERY<small>ギャラリー</small></h2>
    <div class="gallery-row">
      <div class="photo" role="img" aria-label="赤い着物の子どもの写真" style="background:linear-gradient(160deg,#c75a4e,#a8433a)"></div>
      <div class="photo" role="img" aria-label="晴れ着の姉妹の写真" style="background:linear-gradient(160deg,#d98d70,#b96a52)"></div>
      <div class="photo" role="img" aria-label="和装の子どもの写真" style="background:linear-gradient(160deg,#b5544a,#8f3c33)"></div>
      <div class="photo" role="img" aria-label="七五三の記念写真" style="background:linear-gradient(160deg,#e0a283,#c47c5e)"></div>
    </div>
    <span class="btn">MORE</span>
    <div class="gallery-row">
      <div class="photo" role="img" aria-label="家族の記念写真" style="background:linear-gradient(160deg,#a08c78,#7d6a58)"></div>
      <div class="photo" role="img" aria-label="子どもの笑顔の写真" style="background:linear-gradient(160deg,#d06f5f,#b25246)"></div>
      <div class="photo" role="img" aria-label="屋外で遊ぶ子どもの写真" style="background:linear-gradient(160deg,#aeb982,#8a985e)"></div>
      <div class="photo" role="img" aria-label="ベビーの記念写真" style="background:linear-gradient(160deg,#c99a80,#a97a62)"></div>
    </div>
    <span class="btn">MORE</span>
  </section>

  <section class="kids">
    <div class="photo" role="img" aria-label="元気に遊ぶ子どもの写真" style="background:linear-gradient(160deg,#d8c04a,#8fa85a)"></div>
    <div class="photo" role="img" aria-label="笑顔のキッズ写真" style="background:linear-gradient(160deg,#6f8a4c,#3f3a33)"></div>
    <div class="side">
      <h2 class="sec-title">キッズ・ベビー<small>KIDS &amp; BABY</small></h2>
      <p class="txt">元気いっぱいなお子さまの<br>撮影はお任せください</p>
      <span class="btn">MORE</span>
    </div>
  </section>

  <section class="staff">
    <div class="photo" role="img" aria-label="スタッフの集合写真" style="height:64px;background:linear-gradient(135deg,#f0ece6,#9c928a)"></div>
    <div>
      <h2 class="sec-title">スタッフ紹介<small>STAFF</small></h2>
      <p class="txt">笑顔あふれるスタッフが<br>おもてなしいたします</p>
      <span class="btn">MORE</span>
    </div>
  </section>

  <section class="info">
    <div>
      <h2 class="sec-title">ニュース<small>NEWS</small></h2>
      <ul class="list">
        <li>2024.04.01 営業時間のお知らせ</li>
        <li>2024.03.15 春の撮影会のご案内</li>
        <li>2024.02.20 定休日のお知らせ</li>
      </ul>
    </div>
    <div>
      <h2 class="sec-title">ブログ<small>BLOG</small></h2>
      <div class="thumbs">
        <div class="photo" role="img" aria-label="ブログ記事の写真" style="background:#c9b39c"></div>
        <div class="photo" role="img" aria-label="ブログ記事の写真" style="background:#a8b98a"></div>
        <div class="photo" role="img" aria-label="ブログ記事の写真" style="background:#b7a391"></div>
      </div>
    </div>
  </section>

  <section class="contact">
    <div class="tel">
      <svg width="12" height="12" viewBox="0 0 24 24" aria-hidden="true"><path fill="currentColor" d="M6.6 10.8a15.1 15.1 0 0 0 6.6 6.6l2.2-2.2c.3-.3.7-.4 1-.2 1.1.4 2.3.6 3.6.6.6 0 1 .4 1 1V20c0 .6-.4 1-1 1A17 17 0 0 1 3 4c0-.6.4-1 1-1h3.5c.6 0 1 .4 1 1 0 1.3.2 2.5.6 3.6.1.3 0 .7-.2 1z"/></svg>
      <div><small>お電話でのご予約・お問い合わせ</small>0000-00-0000</div>
    </div>
    <span class="btn">お問い合わせ</span>
  </section>

  <footer class="footer">
    <div>
      <div class="name"><i></i>写真館</div>
      <p class="txt">〒000-0000 市内町1-2-3<br>営業 10:00〜18:00 / 火曜定休</p>
    </div>
    <div class="map" role="img" aria-label="店舗周辺の地図"></div>
  </footer>
</main>

<p class="fv-label">ファーストビュー他2枚</p>
<div class="fv fv-1" role="img" aria-label="緑の中で笑う母と子の写真"></div>
<div class="fv fv-2" role="img" aria-label="笑顔の赤ちゃんの写真">
  <p class="fv-copy">季節限定!<br><b>キャンペーンフォト</b></p>
</div>

</body>
</html>
```